Redesign of Business Card to look more professional and stand out

Business card design. You can lean more about our company by going to dkrfabworks.example. Raised letters would be nice. Company name & Address
DK&R
418 Wendlow Ridge Drive, Suite 340
Halverton, OH 44871

You can use my name and title: Glenn Harwick
Business Development Manager

Target Market(s)

Heavy Industrial market, i.e. utilities, chemical plants, paper mills, construction companies

Industry/Entity Type

Construction

Contact Information for Business Card

We provide Project Management & Project Support Services

Font styles to use
Serif

Requirements
Must have
• Company name & Address
• DK&R
• 418 Wendlow Ridge Drive, Suite 340
• Halverton, OH 44871
Nice to have
• ideas for the back of the card
Should not have
• no crazy colors. needs to look professional and standout.

```html
<!DOCTYPE html>
<html lang="en">
<head>
<meta charset="utf-8">
<title>DK&amp;R Business Card</title>
<link href="https://fonts.googleapis.com/css2?family=Tinos:wght@400;700&display=swap" rel="stylesheet">
<style>
  :root {
    --backdrop: #2e2c2d;
    --paper: #ffffff;
    --navy: #1e3564;
    --rust: #c2501c;
    --ink-light: #ffffff;
  }
  html, body {
    margin: 0;
    width: 1200px;
    height: 900px;
    overflow: hidden;
    background: var(--backdrop);
    font-family: "Tinos", "Times New Roman", serif;
  }
  .canvas {
    position: relative;
    width: 1200px;
    height: 900px;
  }
  .card {
    position: absolute;
    left: 285px;
    width: 630px;
    height: 360px;
    background: var(--paper);
    overflow: hidden;
    box-shadow: 0 10px 30px rgba(0,0,0,0.45);
  }
  .card-front { top: 50px; }
  .card-back { top: 490px; }

  .wordmark {
    font-weight: 700;
    color: var(--navy);
    letter-spacing: 2px;
    line-height: 1;
    margin: 0;
  }
  .card-front .wordmark {
    position: absolute;
    left: 0; right: 0;
    top: 128px;
    text-align: center;
    font-size: 104px;
  }
  .card-back .wordmark {
    position: absolute;
    left: 44px;
    top: 40px;
    font-size: 84px;
  }
  .back-shapes {
    position: absolute;
    inset: 0;
  }
  .contact-list {
    position: absolute;
    left: 40px;
    top: 208px;
    margin: 0;
    padding: 0;
    list-style: none;
    color: var(--ink-light);
    font-size: 14px;
    font-weight: 700;
  }
  .contact-list li {
    display: flex;
    align-items: center;
    gap: 12px;
    height: 22px;
  }
  .contact-list svg { width: 13px; height: 13px; fill: var(--ink-light); }
  .holder {
    position: absolute;
    left: 420px;
    top: 150px;
    color: var(--ink-light);
  }
  .holder-name {
    margin: 0;
    font-size: 19px;
    font-weight: 700;
  }
  .holder-title {
    margin: 2px 0 0;
    font-size: 11.5px;
    font-weight: 700;
  }
  .address {
    position: absolute;
    left: 330px;
    top: 236px;
    margin: 0;
    color: var(--ink-light);
    font-style: normal;
    font-size: 16px;
    font-weight: 700;
    line-height: 1.55;
  }
  .address-company {
    display: flex;
    align-items: center;
    gap: 12px;
  }
  .address-company svg { width: 15px; height: 15px; fill: var(--ink-light); }
</style>
</head>
<body>
<main class="canvas">

  <section class="card card-front" aria-label="Card front">
    <h1 class="wordmark">DK&amp;R</h1>
  </section>

  <section class="card card-back" aria-label="Card back">
    <svg class="back-shapes" width="630" height="360" viewBox="0 0 630 360" aria-hidden="true">
      <polygon fill="var(--navy)" points="0,170 630,205 630,360 0,360"/>
      <path fill="var(--navy)" d="M305,189 L340,150 Q346,143 356,143 L630,158 L630,206 Z"/>
      <line x1="0" y1="170" x2="630" y2="205" stroke="var(--rust)" stroke-width="2.5"/>
    </svg>

    <h2 class="wordmark">DK&amp;R</h2>

    <div class="holder">
      <p class="holder-name">Glenn Harwick</p>
      <p class="holder-title">Business Development Manager</p>
    </div>

    <ul class="contact-list">
      <li>
        <svg viewBox="0 0 24 24"><path d="M6.6 10.8a15.1 15.1 0 0 0 6.6 6.6l2.2-2.2a1 1 0 0 1 1-.25 11.4 11.4 0 0 0 3.6.57 1 1 0 0 1 1 1V20a1 1 0 0 1-1 1A17 17 0 0 1 3 4a1 1 0 0 1 1-1h3.5a1 1 0 0 1 1 1 11.4 11.4 0 0 0 .57 3.6 1 1 0 0 1-.25 1Z"/></svg>
        555-014-8273
      </li>
      <li>
        <svg viewBox="0 0 24 24"><path d="M2 5h20v14H2Zm2 2v.5l8 5 8-5V7Zm0 2.8V17h16V9.8l-8 5Z"/></svg>
        info@dkrfabworks.example
      </li>
      <li>
        <svg viewBox="0 0 24 24"><path d="M10.6 13.4a1 1 0 0 1 0-1.4l4-4a1 1 0 1 1 1.4 1.4l-4 4a1 1 0 0 1-1.4 0ZM7.8 20.5a4.3 4.3 0 0 1-3-7.3l2.8-2.8 1.4 1.4-2.8 2.8a2.3 2.3 0 0 0 3.2 3.2l2.8-2.8 1.4 1.4-2.8 2.8a4.3 4.3 0 0 1-3 1.3Zm8.6-6.9-1.4-1.4 2.8-2.8a2.3 2.3 0 0 0-3.2-3.2l-2.8 2.8-1.4-1.4 2.8-2.8a4.3 4.3 0 0 1 6 6Z"/></svg>
        www.dkrfabworks.example
      </li>
    </ul>

    <address class="address">
      <span class="address-company">
        <svg viewBox="0 0 24 24"><path d="M12 3 2 12h3v8h5v-5h4v5h5v-8h3Z"/></svg>
        DK&amp;R
      </span>
      418 Wendlow Ridge Drive,<br>
      Suite 340 Halverton, OH 44871
    </address>
  </section>

</main>
</body>
</html>
```